We need to design Labels of one of Our Brand BrivaLune Lotion.

The purpose of this product is to keep mosquitoes away.
There are 3 variants of this lotion. So we need 3 designs for the product. These variants details are mentioned below:

1) Mosquito Repellent Lotion with Lavender Fragrance.
2) Mosquito Repellent Lotion with Natural Ingredients.
3) Mosquito Repellent Lotion for kids.

Kindly note the bottle will be WHITE for all the variants. Cap will of the bottle will be with accordance to the color of label. In the picture it is red just for presentation.

Kindly share design of Repellent Lotion with Lavendar Fragrance initially and if we give your positive feedback, then you may add further variants of the design.

The bottle shape is attached along with keylines. Also attaching logo. If there is any other option for logo, you can suggest which we would probably keep our existing logo.

Target Market(s)

B+, B, C+

Industry/Entity Type

Product

Colors
a54499
6b449b

Requirements
Must have
• Mosquito
• 100ml
Nice to have
• Purple color as background
Should not have
• Lavendar flower

```html
<!DOCTYPE html>
<html lang="en">
<head>
<meta charset="utf-8">
<title>BrivaLune Mosquito Repellent Lotion – Lavender Label</title>
<link rel="stylesheet" href="https://fonts.googleapis.com/css2?family=Open+Sans:wght@600;700;800&family=Oswald:wght@700&display=swap">
<style>
  :root {
    --page: #ffffff;
    --purple-deep: #6b2a93;
    --purple-mid: #a54499;
    --purple-light: #d58fd6;
    --band: #6a1a86;
    --band-line: #3f0c55;
    --yellow: #d9d62a;
    --yellow-text: #4a2175;
    --blue-dark: #1d5fa8;
    --blue-light: #3fb2e6;
    --white: #ffffff;
    --title-grey: #ece6ef;
  }
  html, body {
    margin: 0;
    width: 1200px;
    height: 1109px;
    overflow: hidden;
    background: var(--page);
  }
  .canvas {
    position: relative;
    width: 1200px;
    height: 1109px;
  }
  .label {
    position: absolute;
    left: 330px;
    top: 35px;
    width: 540px;
    height: 1040px;
    font-family: "Open Sans", Arial, sans-serif;
    color: var(--white);
  }
  .label-art {
    position: absolute;
    inset: 0;
  }
  .brand-name {
    position: absolute;
    left: 40px;
    right: 40px;
    top: 185px;
    text-align: center;
    font-weight: 800;
    font-size: 78px;
    line-height: 1;
    color: var(--white);
    letter-spacing: -1px;
  }
  .product-title {
    position: absolute;
    left: 0;
    right: 0;
    top: 352px;
    text-align: center;
    font-family: "Oswald", "Arial Narrow", sans-serif;
    font-weight: 700;
    color: var(--title-grey);
    text-shadow: 0 2px 0 #5a2a6e;
    line-height: 1.12;
  }
  .product-title .line-main { display: block; font-size: 54px; }
  .product-title .line-sub { display: block; font-size: 54px; }
  .duration-band {
    position: absolute;
    left: 0;
    right: 0;
    top: 510px;
    height: 86px;
    background: var(--band);
    border-top: 4px solid var(--band-line);
    border-bottom: 4px solid var(--band-line);
    display: flex;
    align-items: center;
    justify-content: center;
    gap: 10px;
    font-weight: 700;
    font-size: 30px;
    letter-spacing: 1.5px;
    color: var(--title-grey);
  }
  .duration-number {
    width: 62px;
    height: 62px;
    border: 4px solid var(--white);
    border-radius: 50%;
    display: flex;
    align-items: center;
    justify-content: center;
    font-size: 42px;
    font-weight: 800;
    color: var(--white);
    box-sizing: border-box;
  }
  .protection-seal {
    position: absolute;
    left: 165px;
    top: 620px;
    width: 210px;
    height: 210px;
    border-radius: 50%;
    background: radial-gradient(circle, #f3eef5 0 58%, #4a1a62 59% 100%);
  }
  .scent {
    position: absolute;
    left: 0;
    right: 0;
    top: 850px;
    text-align: center;
    font-weight: 600;
    font-size: 22px;
    letter-spacing: 4px;
  }
  .warning-box {
    position: absolute;
    left: 118px;
    width: 298px;
    top: 890px;
    height: 76px;
    border: 3px solid #e7d8ea;
    box-sizing: border-box;
    display: flex;
    align-items: center;
    justify-content: center;
    text-align: center;
    font-weight: 600;
    font-size: 19px;
    line-height: 1.25;
  }
  .volume {
    position: absolute;
    left: 0;
    right: 0;
    top: 980px;
    text-align: center;
    font-weight: 700;
    font-size: 26px;
  }
</style>
</head>
<body>
<div class="canvas">
  <div class="label">
    <svg class="label-art" width="540" height="1040" viewBox="0 0 540 1040" aria-hidden="true">
      <defs>
        <linearGradient id="labelFill" x1="0" y1="0" x2="1" y2="1">
          <stop offset="0" stop-color="var(--purple-deep)"/>
          <stop offset="0.45" stop-color="var(--purple-light)"/>
          <stop offset="0.75" stop-color="var(--purple-mid)"/>
          <stop offset="1" stop-color="var(--purple-deep)"/>
        </linearGradient>
        <linearGradient id="bannerFill" x1="0" y1="1" x2="1" y2="0">
          <stop offset="0" stop-color="var(--blue-light)"/>
          <stop offset="1" stop-color="var(--blue-dark)"/>
        </linearGradient>
        <path id="topArc" d="M80,80 Q270,30 460,80"/>
      </defs>
      <path class="label-body" d="M0,108 Q270,30 540,108 L540,990 Q540,1040 490,1040 L50,1040 Q0,1040 0,990 Z" fill="url(#labelFill)"/>
      <path class="top-band" d="M0,72 Q270,-8 540,72 L540,112 Q270,34 0,112 Z" fill="var(--yellow)"/>
      <text font-family="Open Sans, sans-serif" font-weight="800" font-size="20" fill="var(--yellow-text)" text-anchor="middle">
        <textPath href="#topArc" startOffset="50%">DERMATOLOGICALLY TESTED</textPath>
      </text>
      <path class="brand-banner" d="M40,160 Q270,118 500,160 L500,318 Q270,350 40,318 Z" fill="url(#bannerFill)" stroke="#7fb6e6" stroke-width="3"/>
      <g class="new-badge" transform="rotate(-10 110 128)">
        <ellipse cx="110" cy="128" rx="72" ry="38" fill="url(#bannerFill)" stroke="#d8e8f5" stroke-width="3"/>
        <text x="110" y="141" text-anchor="middle" font-family="Open Sans, sans-serif" font-weight="800" font-size="34" fill="#ffffff">NEW!</text>
      </g>
    </svg>

    <div class="brand-name">BrivaLune</div>

    <h1 class="product-title" style="margin:0">
      <span class="line-main">MOSQUITO REPELLENT</span>
      <span class="line-sub">LOTION</span>
    </h1>

    <div class="duration-band">
      <span>REPELS FOR</span>
      <span class="duration-number">4</span>
      <span>HOURS</span>
    </div>

    <div class="protection-seal" role="img" aria-label="Dengue protection seal with crossed-out mosquito illustration"></div>

    <div class="scent">LAVENDER SCENT</div>
    <div class="warning-box">KEEP OUT OF REACH OF<br>CHILDREN AND PETS</div>
    <div class="volume">70 ml</div>
  </div>
</div>
</body>
</html>
```